Letterhead design for ZENTORA company

I need an A4 letterhead design for my company "Zentora Electrical Products". I need the letterhead to match my current logo and business card designs. I would like it to be colourful and match the design of the business card in terms of the flowing line of colour where the information is.  

Target Market(s)

Adults aged 20 - 50 Upper middle class.

Industry/Entity Type

It Company

Requirements
Must have
• Must be A4 size and match my current logo and business card designs. Must be clean simple and eye catching.

• Must have the following information

• Zentora Electrical Products LTD
• 7 Ardley Close
• Chiswick
• London
• England
• W9 3QX
• Company No. 05316429
• VAT No. GB 627150384

• Telephone: 02081594360
• Mobile: 07815062247
• Email: info@zentora-goods.co.uk
Nice to have
• nice to have a wave of colour like the business card.
Should not have
• Should not be a different colour scheme to the business card and logo design.

```html
<!DOCTYPE html>
<html lang="en">
<head>
<meta charset="utf-8">
<title>Zentora Electrical Products – Letterhead</title>
<link rel="stylesheet" href="https://fonts.googleapis.com/css2?family=Carlito:wght@400;700&display=swap">
<style>
  :root {
    --teal-deep: #1a949d;
    --teal-mid: #3cc6c8;
    --teal-soft: #5fe3da;
    --label-cyan: #3ee6e6;
    --ink: #111111;
    --paper-light: #ffffff;
    --paper-grey: #cbcbcb;
    --white: #ffffff;
  }
  html, body {
    margin: 0;
    padding: 0;
    overflow: hidden;
  }
  body {
    width: 850px;
    height: 1200px;
    font-family: "Carlito", "Calibri", sans-serif;
  }
  .letterhead {
    position: relative;
    width: 850px;
    height: 1200px;
    overflow: hidden;
    background:
      radial-gradient(ellipse 520px 760px at 300px 820px, var(--paper-light) 0%, #f6f6f6 40%, #e2e2e2 75%, var(--paper-grey) 100%),
      var(--paper-grey);
  }
  .header-band {
    position: absolute;
    top: 0;
    left: 0;
    width: 850px;
    height: 260px;
  }
  .brand {
    position: absolute;
    top: 52px;
    left: 519px;
    color: var(--white);
    font-weight: 400;
  }
  .brand-name {
    display: block;
    font-size: 68px;
    line-height: 68px;
    letter-spacing: 0.5px;
  }
  .brand-tagline {
    display: block;
    margin-top: 0;
    font-size: 29px;
    line-height: 34px;
    letter-spacing: 2.2px;
  }
  .contact {
    position: absolute;
    right: 197px;
    top: 1068px;
    text-align: right;
    font-size: 10.5px;
    color: var(--ink);
  }
  .contact p {
    margin: 0 0 14.5px;
    line-height: 13px;
  }
  .company-name { font-weight: 700; }
  .label { color: var(--label-cyan); }
  .label-strong { color: var(--label-cyan); font-weight: 700; }
  .number-strong { font-weight: 700; }
  .gap { display: inline-block; width: 10px; }
  .divider {
    position: absolute;
    left: 667px;
    top: 1070px;
    width: 2.5px;
    height: 100px;
    background: var(--label-cyan);
  }
  .registration {
    position: absolute;
    left: 686px;
    top: 1125px;
    font-size: 10.5px;
    color: var(--ink);
  }
  .registration p {
    margin: 0 0 14px;
    line-height: 13px;
  }
</style>
</head>
<body>
  <main class="letterhead">
    <svg class="header-band" viewBox="0 0 850 260" xmlns="http://www.w3.org/2000/svg" role="img" aria-label="Curved teal colour wave across the top of the page">
      <defs>
        <linearGradient id="band-fill" x1="0" y1="0" x2="850" y2="0" gradientUnits="userSpaceOnUse">
          <stop offset="0" stop-color="var(--teal-deep)"/>
          <stop offset="0.5" stop-color="var(--teal-soft)"/>
          <stop offset="1" stop-color="var(--teal-deep)"/>
        </linearGradient>
      </defs>
      <path class="header-band-shape" fill="url(#band-fill)"
            d="M0,4 C120,140 400,246 628,247 C720,248 800,232 850,209 L850,0 L0,0 Z"/>
    </svg>

    <div class="brand">
      <span class="brand-name">ZENTORA</span>
      <span class="brand-tagline">Electrical Products</span>
    </div>

    <section class="contact">
      <p class="company-name">Zentora Electrical Products LTD</p>
      <p>7 Ardley Close , Chiswick , London , England , W9 3QX</p>
      <p><span class="label-strong">Telephone:</span> <span class="number-strong">02081594360</span><span class="gap"></span> <span class="label">Mobile:</span> 07815062247</p>
      <p><span class="label">Email:</span> info@zentora-goods.co.uk</p>
    </section>

    <div class="divider"></div>

    <section class="registration">
      <p>Company No. 05316429</p>
      <p>VAT No. GB 627150384</p>
    </section>
  </main>
</body>
</html>
```